Tri-fold flyer for Managed Services IT company

We need a tri-fold flyer design for our Managed Services IT company. Our website is here: https://pelicanfjordit.net. While we don't have to match our website we do want to incorporate the logo in the flyer. We would like a flyer that is *very* easy and quick to read/skim over and convey our message. Something like these:

https://www.artkestrel.com/design/58203917

https://47sketchyard.com/postcard-flyer-design/contests/create-lead-generating-flyer-postcard-managed-services-company-815243

http://www.marbleoaksystems.com/managed-services-no-cost-one-month/

Target Market(s)

Business to business IT services

Industry/Entity Type

It Service

Font styles to use
Serif
Sans Serif

Requirements
Must have
• *very* easy and quick to read/skim over and convey our message
Should not have
• verbose, lots of text

```html
<!DOCTYPE html>
<html lang="en">
<head>
<meta charset="utf-8">
<title>Tri-fold Flyer – Managed IT, Cloud IT and Security Services</title>
<link rel="stylesheet" href="https://fonts.googleapis.com/css2?family=Montserrat:wght@400;500;600;700;800&display=swap">
<style>
  :root{
    --blue:#2d5292;
    --navy:#233b6e;
    --navy-deep:#1e3464;
    --orange:#ea8120;
    --paper:#eef0f3;
    --white:#ffffff;
    --ink:#22386a;
  }
  *{box-sizing:border-box;margin:0;padding:0}
  html,body{width:1200px;height:834px;overflow:hidden;background:#e9eaec}
  body{font-family:"Montserrat",Arial,sans-serif;color:var(--ink)}
  .flyer{display:flex;width:1200px;height:834px}
  .panel{position:relative;width:400px;height:834px;background:var(--paper);overflow:hidden}
  .panel + .panel{border-left:1px solid rgba(0,0,0,.08)}

  .header{position:absolute;left:0;top:0;width:400px;height:214px;z-index:3}
  .header svg{position:absolute;inset:0}
  .header-content{position:absolute;left:0;right:0;top:34px;text-align:center;color:var(--white)}
  .icon-badge{width:62px;height:62px;border-radius:50%;background:var(--white);margin:0 auto 14px;display:flex;align-items:center;justify-content:center}
  .service-title{font-weight:700;font-size:29px;letter-spacing:1.5px;line-height:1}
  .service-sub{font-weight:600;font-size:26px;letter-spacing:1.5px;color:var(--orange);line-height:1.05}

  .photo{position:absolute;left:0;right:0;top:190px;z-index:1}
  .photo .fill{position:absolute;inset:0}
  .pitch{position:absolute;left:0;right:0;z-index:2;text-align:center;padding:0 34px}
  .pitch .lead{font-weight:500;font-size:22px}
  .pitch .claim{font-weight:800;font-size:30px;line-height:1.08;letter-spacing:.5px;text-transform:uppercase;margin:4px 0 8px}
  .pitch .tail{font-weight:500;font-size:19px;line-height:1.25}

  .features-band{position:absolute;left:0;right:0;z-index:2;background:var(--blue);color:var(--white);text-align:center;font-weight:700;font-size:22px;letter-spacing:1.5px;border-bottom:3px solid var(--orange)}
  .feature-list{position:absolute;left:0;right:0;z-index:2;list-style:none}
  .feature-list li{display:flex;align-items:center;gap:10px;font-weight:700}
  .feature-list svg{flex:none}

  /* Managed IT */
  .managed .photo{height:300px}
  .managed .pitch{top:300px}
  .managed .features-band{top:490px;height:70px;line-height:67px}
  .managed .feature-list{top:596px;padding-left:48px}
  .managed .feature-list li{font-size:23px;margin-bottom:16px}

  /* Cloud IT */
  .cloud{background:var(--navy-deep)}
  .cloud .photo{height:300px}
  .cloud .pitch{top:252px}
  .cloud .pitch .lead{font-size:22px}
  .cloud .pitch .claim{font-size:28px}
  .cloud .features-zone{position:absolute;left:0;right:0;top:490px;bottom:0;background:var(--navy-deep);z-index:2}
  .cloud .features-band{position:relative;background:transparent;height:64px;line-height:62px;border-bottom:2px solid var(--orange);margin:0 40px}
  .cloud .feature-list{position:relative;padding:24px 0 0 48px;color:var(--white)}
  .cloud .feature-list li{font-size:16px;font-weight:600;margin-bottom:16px}

  /* Security */
  .security .photo{height:250px}
  .security .pitch{top:244px}
  .security .pitch .lead{font-size:20px}
  .security .pitch .claim{font-size:29px;margin:2px 0 6px}
  .security .pitch .tail{font-size:18px}
  .security .features-band{top:440px;height:66px;line-height:63px}
  .security .feature-list{top:540px;padding-left:40px}
  .security .feature-list li{font-size:16.5px;margin-bottom:17px}
</style>
</head>
<body>
<main class="flyer">

  <!-- Managed IT Services -->
  <section class="panel managed">
    <div class="header">
      <svg width="400" height="214" viewBox="0 0 400 214">
        <polygon points="0,0 400,0 400,190 228,190 200,210 172,190 0,190" fill="var(--blue)"/>
        <polyline points="0,190 172,190 200,210 228,190 400,190" fill="none" stroke="var(--orange)" stroke-width="4"/>
      </svg>
      <div class="header-content">
        <div class="icon-badge">
          <svg width="34" height="30" viewBox="0 0 34 30"><rect x="2" y="2" width="30" height="19" rx="2" fill="none" stroke="var(--blue)" stroke-width="3"/><rect x="14" y="21" width="6" height="5" fill="var(--blue)"/><rect x="9" y="26" width="16" height="3" rx="1" fill="var(--blue)"/></svg>
        </div>
        <div class="service-title">MANAGED IT</div>
        <div class="service-sub">SERVICES</div>
      </div>
    </div>
    <div class="photo"><div class="fill" role="img" aria-label="Soft-focus photo of an office desk with a computer" style="background:linear-gradient(180deg,#cfd3d8 0%,#e3e5e8 45%,#eef0f3 100%)"></div></div>
    <div class="pitch">
      <div class="lead">Strategically</div>
      <div class="claim">Optimize and<br>protect</div>
      <div class="tail">your infrastructure with<br>24/7 proactive Monitoring.</div>
    </div>
    <div class="features-band">FEATURES</div>
    <ul class="feature-list">
      <li><svg width="18" height="16" viewBox="0 0 18 16"><path d="M2 8l5 5L16 2" fill="none" stroke="var(--orange)" stroke-width="3.5"/></svg>Budget Your IT</li>
      <li><svg width="18" height="16" viewBox="0 0 18 16"><path d="M2 8l5 5L16 2" fill="none" stroke="var(--orange)" stroke-width="3.5"/></svg>Reduce Costly Downtime</li>
      <li><svg width="18" height="16" viewBox="0 0 18 16"><path d="M2 8l5 5L16 2" fill="none" stroke="var(--orange)" stroke-width="3.5"/></svg>Dependable Service</li>
    </ul>
  </section>

  <!-- Cloud IT Services -->
  <section class="panel cloud">
    <div class="header">
      <svg width="400" height="214" viewBox="0 0 400 214">
        <polygon points="0,0 400,0 400,190 228,190 200,210 172,190 0,190" fill="var(--navy)"/>
        <polyline points="0,190 172,190 200,210 228,190 400,190" fill="none" stroke="var(--orange)" stroke-width="4"/>
      </svg>
      <div class="header-content">
        <div class="icon-badge">
          <svg width="36" height="28" viewBox="0 0 36 28"><path d="M9 22a7 7 0 0 1 0-14 9 9 0 0 1 17-1 7.5 7.5 0 0 1 1 15z" fill="var(--navy)"/><path d="M18 24V12M13 16l5-5 5 5" fill="none" stroke="var(--white)" stroke-width="2.5"/></svg>
        </div>
        <div class="service-title">CLOUD IT</div>
        <div class="service-sub">SERVICES</div>
      </div>
    </div>
    <div class="photo"><div class="fill" role="img" aria-label="Photo of hands typing on a laptop beside a printed bar chart report" style="background:linear-gradient(180deg,#c9d3e0 0%,#dfe5ed 55%,#eef1f5 100%)"></div></div>
    <div class="pitch">
      <div class="lead">Cloud IT is the</div>
      <div class="claim">Future of<br>small &amp; medium</div>
      <div class="tail">business technology<br>management.</div>
    </div>
    <div class="features-zone">
      <div class="features-band">FEATURES</div>
      <ul class="feature-list">
        <li><svg width="16" height="14" viewBox="0 0 18 16"><path d="M2 8l5 5L16 2" fill="none" stroke="var(--orange)" stroke-width="3.5"/></svg>Hosted Postwell Exchange</li>
        <li><svg width="16" height="14" viewBox="0 0 18 16"><path d="M2 8l5 5L16 2" fill="none" stroke="var(--orange)" stroke-width="3.5"/></svg>Hosted Server Solutions</li>
        <li><svg width="16" height="14" viewBox="0 0 18 16"><path d="M2 8l5 5L16 2" fill="none" stroke="var(--orange)" stroke-width="3.5"/></svg>Virtualized Desktop Solutions</li>
        <li><svg width="16" height="14" viewBox="0 0 18 16"><path d="M2 8l5 5L16 2" fill="none" stroke="var(--orange)" stroke-width="3.5"/></svg>Hardware Virtualization</li>
        <li><svg width="16" height="14" viewBox="0 0 18 16"><path d="M2 8l5 5L16 2" fill="none" stroke="var(--orange)" stroke-width="3.5"/></svg>Cloud Backup and Security</li>
        <li><svg width="16" height="14" viewBox="0 0 18 16"><path d="M2 8l5 5L16 2" fill="none" stroke="var(--orange)" stroke-width="3.5"/></svg>Boxwren Storage for Business</li>
      </ul>
    </div>
  </section>

  <!-- Security Services -->
  <section class="panel security">
    <div class="header">
      <svg width="400" height="214" viewBox="0 0 400 214">
        <polygon points="0,0 400,0 400,190 228,190 200,210 172,190 0,190" fill="var(--blue)"/>
        <polyline points="0,190 172,190 200,210 228,190 400,190" fill="none" stroke="var(--orange)" stroke-width="4"/>
      </svg>
      <div class="header-content">
        <div class="icon-badge">
          <svg width="28" height="32" viewBox="0 0 28 32"><path d="M7 14V9a7 7 0 0 1 14 0v5" fill="none" stroke="var(--blue)" stroke-width="3.5"/><rect x="3" y="14" width="22" height="16" rx="2" fill="var(--blue)"/><circle cx="14" cy="21" r="2.5" fill="var(--white)"/><rect x="13" y="22" width="2" height="5" fill="var(--white)"/></svg>
        </div>
        <div class="service-title">SECURITY</div>
        <div class="service-sub">SERVICES</div>
      </div>
    </div>
    <div class="photo"><div class="fill" role="img" aria-label="Close-up photo of a hand typing on a laptop keyboard" style="background:linear-gradient(180deg,#e6d6cc 0%,#eee3dc 50%,#f1ece8 100%)"></div></div>
    <div class="pitch">
      <div class="lead">Advanced security systems</div>
      <div class="claim">Help protect<br>your data</div>
      <div class="tail">and keep your business<br>up and running.</div>
    </div>
    <div class="features-band">FEATURES</div>
    <ul class="feature-list">
      <li><svg width="16" height="14" viewBox="0 0 18 16"><path d="M2 8l5 5L16 2" fill="none" stroke="var(--orange)" stroke-width="3.5"/></svg>Unified Threat Management</li>
      <li><svg width="16" height="14" viewBox="0 0 18 16"><path d="M2 8l5 5L16 2" fill="none" stroke="var(--orange)" stroke-width="3.5"/></svg>Web Filtering &amp; Firewall</li>
      <li><svg width="16" height="14" viewBox="0 0 18 16"><path d="M2 8l5 5L16 2" fill="none" stroke="var(--orange)" stroke-width="3.5"/></svg>Spam Protection</li>
      <li><svg width="16" height="14" viewBox="0 0 18 16"><path d="M2 8l5 5L16 2" fill="none" stroke="var(--orange)" stroke-width="3.5"/></svg>Digital Security Camera Systems</li>
      <li><svg width="16" height="14" viewBox="0 0 18 16"><path d="M2 8l5 5L16 2" fill="none" stroke="var(--orange)" stroke-width="3.5"/></svg>Sentrel Security Solutions</li>
      <li><svg width="16" height="14" viewBox="0 0 18 16"><path d="M2 8l5 5L16 2" fill="none" stroke="var(--orange)" stroke-width="3.5"/></svg>Email Protection</li>
    </ul>
  </section>

</main>
</body>
</html>
```